Podiatry Clinic needs an A0 poster design

we need an A0 poster design for our clinic frontage to include our logo and a feet theme. it is located either in a frame on a glass wall, or in a freestanding poster holder within a shopping centre.
Our clinic values are integrity, respect, excellence, happiness and fun.
We want to let people know that if your feet fail you, then the rest of you slows down very quickly, so get your feet checked immediately. we deal with kids feet, sporty feet, mature feet.

Target Market(s)

parents with kids

Industry/Entity Type

Medical

Requirements
Must have
• Marlow Stride Clinic Logo
• www.marlowstrideclinic.net
• 7261 8092
• easy to read from a distance
Nice to have
• fun, friendly, inviting, colourful, happy.
Should not have
• cartoon
• ugly
• sad
• not too much text
• no fanciful fonts

```html
<!DOCTYPE html>
<html lang="en">
<head>
<meta charset="utf-8">
<title>Marlow Stride Clinic – Poster</title>
<link rel="stylesheet" href="https://fonts.googleapis.com/css2?family=Arimo:ital,wght@0,400;0,700;1,700&family=Open+Sans:wght@700&display=swap">
<style>
  :root {
    --clinic-blue: #0071bc;
    --clinic-orange: #f07022;
    --paper: #ffffff;
    --edge: #e2e2e2;
    --skin-light: #f6dccb;
    --skin-mid: #eeb99a;
    --skin-warm: #e59f86;
    --sheet: #f8f6f4;
  }
  html, body {
    margin: 0;
    padding: 0;
    width: 1200px;
    height: 1200px;
    overflow: hidden;
    background: var(--paper);
  }
  .poster-canvas { display: block; width: 1200px; height: 1200px; }
  .poster-sheet { fill: var(--paper); stroke: var(--edge); stroke-width: 2; }
  .band-blue { fill: var(--clinic-blue); }
  .band-orange { fill: var(--clinic-orange); }
  .band-white { fill: var(--paper); }
  .headline {
    font-family: "Arimo", Arial, sans-serif;
    font-weight: 700;
    font-style: italic;
    fill: var(--clinic-blue);
    font-size: 42px;
  }
  .phone {
    font-family: "Open Sans", Arial, sans-serif;
    font-weight: 700;
    fill: var(--paper);
    font-size: 80px;
  }
  .web {
    font-family: "Arimo", Arial, sans-serif;
    font-weight: 700;
    fill: var(--paper);
    font-size: 40px;
  }
  .brand-mark { fill: var(--clinic-blue); }
  .brand-name {
    font-family: "Arimo", Arial, sans-serif;
    font-weight: 400;
    fill: var(--clinic-blue);
    font-size: 36px;
  }
</style>
</head>
<body>
<svg class="poster-canvas" viewBox="0 0 1500 1500" xmlns="http://www.w3.org/2000/svg">
  <defs>
    <linearGradient id="skinTone" x1="0" y1="0" x2="1" y2="1">
      <stop offset="0" stop-color="var(--sheet)"/>
      <stop offset="0.3" stop-color="var(--skin-mid)"/>
      <stop offset="0.6" stop-color="var(--skin-light)"/>
      <stop offset="1" stop-color="var(--skin-warm)"/>
    </linearGradient>
  </defs>

  <rect class="poster-sheet" x="240" y="28" width="1020" height="1442"/>

  <rect class="hero-photo" x="250" y="60" width="1010" height="785" fill="url(#skinTone)"
        role="img" aria-label="Close-up photo of a baby's bare feet on a white sheet"/>

  <path class="band-blue" d="M240,28 H1260 V95 C1150,250 1060,310 980,303 C870,295 790,160 700,100 C640,65 560,70 420,110 L255,183 L240,190 Z"/>
  <path class="band-blue" d="M240,260 C380,220 480,120 580,113 C700,108 780,240 880,320 C950,375 1010,392 1070,383 C1140,370 1190,300 1215,237 C1180,320 1120,365 1040,362 C970,360 920,330 850,270 C770,200 700,140 585,140 C480,140 380,175 240,205 Z"/>

  <text class="headline" x="252" y="718">Free your feet</text>
  <text class="headline" x="272" y="780">at the Marlow Stride Clinic.</text>

  <text class="headline" x="324" y="902">Your family and</text>
  <text class="headline" x="396" y="969">sports podiatrists!</text>

  <path class="band-orange" d="M240,1272 C340,1240 420,1160 500,1105 C560,1060 620,1025 680,1035 C770,1050 820,1140 880,1225 C950,1310 1050,1340 1260,1345 V1470 H240 Z"/>
  <path class="band-white" d="M450,1098 C540,1040 630,1040 690,1075 C750,1115 800,1220 850,1300 C900,1375 980,1392 1200,1403 C980,1418 880,1405 830,1340 C780,1270 730,1160 680,1110 C620,1060 540,1060 450,1098 Z"/>

  <text class="phone" x="344" y="1333">7261 8092</text>
  <text class="web" x="270" y="1411">www.marlowstrideclinic.net</text>

  <g class="clinic-brand">
    <circle class="brand-mark" cx="1052" cy="1012" r="120"/>
    <text class="brand-name" x="1052" y="1188" text-anchor="middle">Marlow Stride Clinic</text>
  </g>
</svg>
</body>
</html>
```